Stationery Design needed for logo design project

This project is linked to Professional firm of accountants need a make over. Our company needs a Stationery Design. Please refer to our original project in the link above.

Industry/Entity Type

It Company

Requirements
Must have
• We have three offices , so headed note paper for each office seperately
Nice to have
• we like clean uncomplicated designs, as we are happy with the logo as is and don't want to distract from it
Should not have
• there needs to be a legend at the bottom of the paper setting out our obligations under the league of vantmere fiscal stewards

```html
<!DOCTYPE html>
<html lang="en">
<head>
<meta charset="utf-8">
<title>Brennick Chartered Accountants – Stationery Set</title>
<link rel="stylesheet" href="https://fonts.googleapis.com/css2?family=Lato:wght@300;400;700&display=swap">
<style>
  :root {
    --board: #b4b4b4;
    --paper: #ffffff;
    --ink: #3a3a3a;
    --grey: #6d6869;
    --grey-light: #8a8a8a;
    --green: #127a3a;
    --green-bright: #39b54a;
    --green-deep: #15663a;
    --black-card: #0b0b0b;
    --shadow: 0 2px 4px rgba(0,0,0,.35);
  }
  * { box-sizing: border-box; margin: 0; padding: 0; }
  html, body { width: 1200px; height: 640px; overflow: hidden; }
  body {
    position: relative;
    background: var(--board);
    font-family: "Lato", "Helvetica Neue", Arial, sans-serif;
    color: var(--ink);
  }
  .piece {
    position: absolute;
    left: var(--x); top: var(--y); width: var(--w); height: var(--h);
    background: var(--paper);
    box-shadow: var(--shadow);
    overflow: hidden;
  }
  .piece--dark { background: var(--black-card); color: #fff; }

  .brand { position: absolute; display: flex; align-items: center; gap: 6px; }
  .brand__square { width: var(--sq, 14px); height: var(--sq, 14px); background: var(--green); flex: none; }
  .brand__name { font-weight: 300; color: var(--grey); font-size: var(--fs, 18px); line-height: 1; letter-spacing: .5px; }
  .piece--dark .brand__name { color: var(--grey-light); }

  .holder { position: absolute; text-align: right; }
  .holder__name { font-weight: 700; font-size: 11px; color: #111; }
  .holder__role { font-weight: 400; font-size: 6.5px; color: var(--grey); }
  .piece--dark .holder__name { color: var(--green-bright); }
  .piece--dark .holder__role { color: var(--grey-light); }
  .rule { position: absolute; height: 1px; background: var(--green); }

  .contact { position: absolute; list-style: none; font-size: 6.6px; line-height: 8.6px; color: #222; }
  .piece--dark .contact { color: #fff; }
  .contact li { display: flex; align-items: center; gap: 4px; }
  .contact__icon { width: 4px; height: 4px; border-radius: 50%; background: var(--green); flex: none; }
  .address { position: absolute; font-size: 6.6px; line-height: 8px; color: #222; }
  .piece--dark .address { color: #fff; }

  .motif {
    position: absolute; width: var(--s); height: var(--s); right: var(--r); bottom: var(--b);
    background: linear-gradient(135deg, rgba(57,181,74,.35), rgba(200,200,200,.25));
  }
  .piece--dark .motif { background: linear-gradient(135deg, rgba(57,181,74,.35), rgba(90,90,90,.35)); }
  .motif--faint { background: linear-gradient(135deg, rgba(57,181,74,.14), rgba(210,210,210,.18)); }

  .wave { position: absolute; left: 0; bottom: 0; width: 100%; display: block; }

  .slip-title { position: absolute; right: 4px; top: 6px; font-size: 8px; font-weight: 700; color: var(--green); }
  .micro { position: absolute; font-size: 3.6px; line-height: 4.6px; color: var(--grey); white-space: nowrap; }
  .micro--divided { border-left: 1px solid #bbb; padding-left: 4px; }

  .letterhead .brand { left: 18px; top: 4px; --fs: 17px; --sq: 14px; }
  .letterhead .micro { left: 197px; top: 3px; }

  .folder { background: var(--green-deep); }
  .folder__text { position: absolute; left: 0; width: 100%; text-align: center; font-size: 3.6px; line-height: 4.6px; color: #d5e8da; }
</style>
</head>
<body>

<!-- Business card, front with details -->
<section class="piece card" style="--x:30px;--y:28px;--w:232px;--h:134px">
  <div class="brand" style="left:16px;top:22px;--fs:17px;--sq:13px"><span class="brand__square"></span><span class="brand__name">brennick</span></div>
  <div class="holder" style="right:10px;top:14px"><p class="holder__name">Marcus Holloway</p><p class="holder__role">Director</p></div>
  <div class="rule" style="left:126px;right:0;top:40px"></div>
  <ul class="contact" style="left:14px;top:64px">
    <li><span class="contact__icon"></span>+0 555.201.7740</li>
    <li><span class="contact__icon"></span>+0 555.201.7740</li>
    <li><span class="contact__icon"></span>office@brennickmail.com</li>
    <li><span class="contact__icon"></span>www.brennickfirm.com</li>
  </ul>
  <p class="address" style="left:14px;top:102px">4/210 Harlow Street, Suite 1<br>PO BOX 4817, Area code, Country</p>
  <div class="motif" style="--s:70px;--r:0;--b:0"></div>
</section>

<!-- Business card, wave version with details -->
<section class="piece card" style="--x:282px;--y:28px;--w:237px;--h:136px">
  <div class="brand" style="left:18px;top:16px;--fs:17px;--sq:13px"><span class="brand__square"></span><span class="brand__name">brennick</span></div>
  <div class="holder" style="right:12px;top:7px"><p class="holder__name">Marcus Holloway</p><p class="holder__role">Director</p></div>
  <ul class="contact" style="left:14px;top:42px">
    <li><span class="contact__icon"></span>+0 555.201.7740</li>
    <li><span class="contact__icon"></span>+0 555.201.7740</li>
    <li><span class="contact__icon"></span>office@brennickmail.com</li>
    <li><span class="contact__icon"></span>www.brennickfirm.com</li>
  </ul>
  <p class="address" style="left:14px;top:78px">4/210 Harlow Street, Suite 1<br>PO BOX 4817, Area code, Country</p>
  <svg class="wave" height="38" viewBox="0 0 300 60" preserveAspectRatio="none" aria-hidden="true">
    <path d="M0 22 C70 4 150 8 300 18 L300 60 L0 60Z" fill="var(--grey)"/>
    <path d="M0 34 C70 16 160 22 300 28 L300 60 L0 60Z" fill="#fff"/>
    <path d="M0 37 C70 20 160 26 300 31 L300 60 L0 60Z" fill="var(--green)"/>
  </svg>
</section>

<!-- Business card, plain white back -->
<section class="piece card" style="--x:30px;--y:182px;--w:234px;--h:134px">
  <div class="brand" style="left:34px;top:52px;--fs:26px;--sq:24px"><span class="brand__square"></span><span class="brand__name">brennick</span></div>
</section>

<!-- Business card, wave back -->
<section class="piece card" style="--x:282px;--y:182px;--w:237px;--h:135px">
  <div class="brand" style="left:30px;top:38px;--fs:26px;--sq:24px"><span class="brand__square"></span><span class="brand__name">brennick</span></div>
  <svg class="wave" height="44" viewBox="0 0 300 60" preserveAspectRatio="none" aria-hidden="true">
    <path d="M0 22 C70 4 150 8 300 18 L300 60 L0 60Z" fill="var(--grey)"/>
    <path d="M0 34 C70 16 160 22 300 28 L300 60 L0 60Z" fill="#fff"/>
    <path d="M0 37 C70 20 160 26 300 31 L300 60 L0 60Z" fill="var(--green)"/>
  </svg>
</section>

<!-- Business card, black front with details -->
<section class="piece piece--dark card" style="--x:30px;--y:334px;--w:234px;--h:134px">
  <div class="brand" style="left:18px;top:22px;--fs:15px;--sq:12px"><span class="brand__square"></span><span class="brand__name">brennick</span></div>
  <div class="holder" style="right:12px;top:14px"><p class="holder__name">Marcus Holloway</p><p class="holder__role">Director</p></div>
  <div class="rule" style="left:126px;right:0;top:39px"></div>
  <ul class="contact" style="left:14px;top:68px">
    <li><span class="contact__icon"></span>+0 555.201.7740</li>
    <li><span class="contact__icon"></span>+0 555.201.7740</li>
    <li><span class="contact__icon"></span>office@brennickmail.com</li>
    <li><span class="contact__icon"></span>www.brennickfirm.com</li>
  </ul>
  <p class="address" style="left:14px;top:104px">4/210 Harlow Street, Suite 1<br>PO BOX 4817, Area code, Country</p>
  <div class="motif" style="--s:70px;--r:0;--b:0"></div>
</section>

<!-- Business card, black back -->
<section class="piece piece--dark card" style="--x:30px;--y:489px;--w:234px;--h:134px">
  <div class="brand" style="left:34px;top:54px;--fs:24px;--sq:22px"><span class="brand__square"></span><span class="brand__name">brennick</span></div>
</section>

<!-- Compliments slip -->
<section class="piece slip" style="--x:282px;--y:350px;--w:245px;--h:110px">
  <div class="brand" style="left:14px;top:12px;--fs:11px;--sq:9px"><span class="brand__square"></span><span class="brand__name">brennick</span></div>
  <p class="micro micro--divided" style="left:76px;top:13px">8 Calder House, Orwell Lane<br>Merrow Business Park, Eastford</p>
  <p class="slip-title">With Compliments</p>
  <div class="motif motif--faint" style="--s:62px;--r:12px;--b:34px"></div>
  <svg class="wave" height="36" viewBox="0 0 300 60" preserveAspectRatio="none" aria-hidden="true">
    <path d="M0 22 C70 4 150 8 300 18 L300 60 L0 60Z" fill="var(--grey)"/>
    <path d="M0 34 C70 16 160 22 300 28 L300 60 L0 60Z" fill="#fff"/>
    <path d="M0 37 C70 20 160 26 300 31 L300 60 L0 60Z" fill="var(--green)"/>
  </svg>
</section>

<!-- Letterheads, one per office, stacked -->
<section class="piece letterhead letterhead--office-3" style="--x:539px;--y:20px;--w:285px;--h:370px">
  <div class="brand"><span class="brand__square"></span><span class="brand__name">brennick</span></div>
  <p class="micro micro--divided">020 7000 5678<br>www.brennickfirm.com<br>3 Ashby Court, Fenwick Road<br>Northgate Park, Haddon</p>
</section>

<section class="piece letterhead letterhead--office-2" style="--x:539px;--y:44px;--w:285px;--h:370px">
  <div class="brand"><span class="brand__square"></span><span class="brand__name">brennick</span></div>
  <p class="micro micro--divided">020 7000 3456<br>www.brennickfirm.com<br>12 Linden Row, Tallis Street<br>Riverside Quarter, Carlow</p>
</section>

<section class="piece letterhead letterhead--office-1" style="--x:539px;--y:68px;--w:285px;--h:370px">
  <div class="brand"><span class="brand__square"></span><span class="brand__name">brennick</span></div>
  <p class="micro micro--divided">020 7000 1234<br>www.brennickfirm.com<br>8 Calder House, Orwell Lane<br>Merrow Business Park, Eastford</p>
  <div class="motif motif--faint" style="--s:80px;--r:100px;--b:150px"></div>
  <svg class="wave" height="38" viewBox="0 0 300 60" preserveAspectRatio="none" aria-hidden="true">
    <path d="M0 20 C70 4 150 10 300 10 L300 60 L0 60Z" fill="var(--grey)"/>
    <path d="M0 34 C70 18 160 24 300 22 L300 60 L0 60Z" fill="#fff"/>
    <path d="M0 37 C70 22 160 28 300 26 L300 60 L0 60Z" fill="var(--green)"/>
  </svg>
</section>

<!-- Presentation folder, laid flat -->
<section class="piece folder" style="--x:838px;--y:38px;--w:341px;--h:310px">
  <svg class="wave" style="top:0;bottom:auto" width="341" height="110" viewBox="0 0 341 110" preserveAspectRatio="none" aria-hidden="true">
    <path d="M0 0 H341 V70 C250 74 170 66 90 92 C50 104 20 108 0 110Z" fill="var(--grey)"/>
    <path d="M0 0 H341 V58 C250 62 170 54 90 80 C50 92 20 96 0 98Z" fill="#fff"/>
  </svg>
  <div class="brand" style="left:220px;top:20px;--fs:17px;--sq:14px"><span class="brand__square"></span><span class="brand__name">brennick</span></div>
  <div class="motif" style="--s:86px;--r:6px;--b:40px;background:linear-gradient(135deg,rgba(57,181,74,.3),rgba(200,200,200,.18))"></div>
  <div class="brand" style="left:142px;top:258px;--fs:9px;--sq:7px"><span class="brand__square"></span><span class="brand__name" style="color:#d5e8da">brennick</span></div>
  <p class="folder__text" style="top:272px">T 020 7000 1234 W brennickfirm.com<br>8 Calder House, Merrow Business Park</p>
</section>

<!-- DL envelope, front -->
<section class="piece envelope" style="--x:428px;--y:472px;--w:342px;--h:151px">
  <div class="brand" style="left:22px;top:20px;--fs:12px;--sq:10px"><span class="brand__square"></span><span class="brand__name">brennick</span></div>
  <p class="micro micro--divided" style="left:100px;top:21px">8 Calder House, Orwell Lane<br>Merrow Business Park, Eastford</p>
  <div class="motif motif--faint" style="--s:84px;--r:50px;--b:42px"></div>
  <svg class="wave" height="40" viewBox="0 0 300 60" preserveAspectRatio="none" aria-hidden="true">
    <path d="M0 26 C70 20 130 10 300 16 L300 60 L0 60Z" fill="var(--grey)"/>
    <path d="M0 40 C70 34 140 22 300 28 L300 60 L0 60Z" fill="#fff"/>
    <path d="M0 43 C70 37 140 26 300 31 L300 60 L0 60Z" fill="var(--green)"/>
  </svg>
</section>

<!-- DL envelope, back -->
<section class="piece envelope" style="--x:808px;--y:474px;--w:334px;--h:149px">
  <svg class="wave" style="top:0;bottom:auto" width="334" height="40" viewBox="0 0 334 40" aria-hidden="true">
    <path d="M4 0 V12 C4 22 12 28 26 30 L308 30 C322 28 330 22 330 12 V0" fill="none" stroke="#9a9a9a" stroke-width=".8"/>
  </svg>
  <div class="brand" style="left:140px;top:10px;--fs:10px;--sq:8px"><span class="brand__square"></span><span class="brand__name">brennick</span></div>
</section>

</body>
</html>
```